Business Card Design

we are a brand new cable TV network devoted to self improvement and leading a better life called FLOURIVO TV.I have a logo. We have 3 executives that need cards.I want it to be a heavy stock card: professional but showing our creative nature

Industry/Entity Type

Business

Contact Information for Business Card

CLAUDIA SAENZ AMLIECEO350 San Juan DrPonte Vedra Beach FL 32082904-473-5953

```html
<!DOCTYPE html>
<html lang="en">
<head>
<meta charset="utf-8">
<title>FLOURIVO TV – Business Card</title>
<link rel="stylesheet" href="https://fonts.googleapis.com/css2?family=Josefin+Sans:wght@300;600&family=Oswald:wght@300;400&display=swap">
<style>
  :root {
    --backdrop: #cdd2d1;
    --charcoal: #2b2a2c;
    --charcoal-light: #3d3c3f;
    --title-grey: #bdbcbd;
    --band-white: #ffffff;
    --accent-yellow: #f8b418;
    --icon-dark: #3a393b;
    --text-light: #ffffff;
    --name-dark: #2b2a2c;
  }
  html, body {
    margin: 0;
    width: 1200px;
    height: 1000px;
    overflow: hidden;
    background: var(--backdrop);
  }
  .business-card {
    position: absolute;
    left: 350px;
    top: 70px;
    width: 500px;
    height: 860px;
    box-shadow: 0 12px 30px rgba(0,0,0,0.25);
  }
  .business-card svg { display: block; }
  .brand-title {
    font-family: "Josefin Sans", sans-serif;
    font-weight: 300;
    fill: var(--title-grey);
    letter-spacing: 4px;
  }
  .brand-wordmark {
    font-family: "Josefin Sans", sans-serif;
    font-weight: 600;
    fill: var(--charcoal);
  }
  .holder-name {
    font-family: "Oswald", sans-serif;
    font-weight: 400;
    fill: var(--name-dark);
    letter-spacing: 0.5px;
  }
  .contact-line {
    font-family: "Oswald", sans-serif;
    font-weight: 300;
    fill: var(--text-light);
    letter-spacing: 0.5px;
  }
</style>
</head>
<body>
  <div class="business-card">
    <svg width="500" height="860" viewBox="0 0 500 860" xmlns="http://www.w3.org/2000/svg">
      <defs>
        <radialGradient id="header-glow" cx="0.5" cy="0.5" r="0.7">
          <stop offset="0" stop-color="#3d3c3f"/>
          <stop offset="1" stop-color="#2b2a2c"/>
        </radialGradient>
        <radialGradient id="pattern-tone" cx="0.5" cy="0.5" r="0.7">
          <stop offset="0" stop-color="#3b3f41"/>
          <stop offset="1" stop-color="#2c2d30"/>
        </radialGradient>
      </defs>

      <rect class="card-header" x="0" y="0" width="500" height="230" fill="url(#header-glow)"/>
      <text class="brand-title" x="250" y="120" font-size="68" text-anchor="middle">FLOURIVO</text>
      <text class="brand-title" x="250" y="200" font-size="68" text-anchor="middle">TV</text>

      <rect class="logo-band" x="0" y="230" width="500" height="80" fill="var(--band-white)"/>
      <rect class="wordmark-square" x="350" y="262" width="16" height="16" fill="var(--charcoal)"/>
      <text class="brand-wordmark" x="374" y="280" font-size="24">Flourivo</text>

      <rect class="pattern-field" x="0" y="310" width="500" height="300" fill="url(#pattern-tone)" role="img" aria-label="Decorative teal dashed diamond pattern on charcoal"/>

      <polygon class="panel-edge" points="0,592 500,512 500,528 0,608" fill="var(--charcoal)"/>
      <polygon class="contact-panel" points="0,606 500,526 500,860 0,860" fill="var(--accent-yellow)"/>
      <polygon class="name-divider" points="110,626 500,626 500,632 104,632" fill="var(--charcoal)"/>
      <text class="holder-name" x="482" y="612" font-size="19" text-anchor="end">MIRELLA OKAFOR DUNST - CEO</text>

      <g class="contact-icon icon-mail">
        <circle cx="75" cy="698" r="22" fill="var(--icon-dark)"/>
        <rect x="64" y="690" width="22" height="15" fill="none" stroke="#ffffff" stroke-width="1.6"/>
        <polyline points="64,690 75,699 86,690" fill="none" stroke="#ffffff" stroke-width="1.6"/>
      </g>
      <text class="contact-line" x="125" y="690" font-size="22">718 Harlow Creek Dr</text>
      <text class="contact-line" x="125" y="720" font-size="22">Larkmere Cove LM 00482</text>

      <g class="contact-icon icon-phone">
        <circle cx="75" cy="775" r="22" fill="var(--icon-dark)"/>
        <path d="M67 768 q2 -3 5 -1 l2 3 q1 2 -1 3 q2 4 5 6 q1 -2 3 -1 l3 2 q2 3 -1 5 q-5 3 -12 -5 q-7 -8 -4 -12 z" fill="#ffffff"/>
      </g>
      <text class="contact-line" x="125" y="783" font-size="22">904-618-2047</text>
    </svg>
  </div>
</body>
</html>
```